11x 11 - KIVO Program Flyer

Introducing The KIVO PROGRAM

The BEST DPA Product on the Planet
* Lowest Zarn in the Industry - 580 Minimum
* Nothing Down - 100% GTU Purchase Financing
* One Submission, One Approval and One Closing
* No Income Limits, No DTI Restrictions, No Property Restrictions

Call (800) 471-9026 for more information

RLCB #738160
www.2ndlanehomes.com

```html
<!DOCTYPE html>
<html lang="en">
<head>
<meta charset="utf-8">
<title>KIVO Program Flyer</title>
<link href="https://fonts.googleapis.com/css2?family=Bebas+Neue&family=Montserrat:wght@400;500;600;700;800&display=swap" rel="stylesheet">
<style>
  :root {
    --blue: #0a5ba3;
    --blue-line: #0b5aa8;
    --gold: #d6c232;
    --olive: #b7a81f;
    --ink: #1d1d1d;
    --white: #ffffff;
    --red: #e3102c;
    --photo-warm-a: #d9cfc3;
    --photo-warm-b: #8a6a52;
    --photo-portrait-a: #3f4a4e;
    --photo-portrait-b: #b98d70;
  }
  * { margin: 0; padding: 0; box-sizing: border-box; }
  html, body { width: 1200px; height: 1200px; overflow: hidden; background: var(--white); }
  .flyer {
    position: relative;
    width: 1200px;
    height: 1200px;
    overflow: hidden;
    font-family: "Montserrat", Arial, sans-serif;
    color: var(--ink);
  }
  .backdrop { position: absolute; inset: 0; width: 1200px; height: 1200px; }

  .brand {
    position: absolute;
    left: 68px; top: 61px;
    width: 390px; height: 231px;
    display: flex; align-items: center; justify-content: center; gap: 14px;
  }
  .brand-dot { width: 34px; height: 34px; border-radius: 50%; background: var(--gold); flex: none; }
  .brand-name { font-weight: 700; font-size: 30px; line-height: 1.1; color: var(--blue); }

  .headline {
    position: absolute;
    left: 64px; top: 318px;
    font-family: "Bebas Neue", Impact, sans-serif;
    color: var(--ink);
    line-height: 0.86;
  }
  .headline .line { display: block; font-size: 98px; letter-spacing: -1px; }
  .headline .line-big { font-size: 140px; letter-spacing: -1px; margin-top: 4px; }
  .headline .accent { color: var(--blue); }

  .offer { position: absolute; left: 68px; top: 736px; color: var(--white); }
  .offer-title { font-weight: 700; font-size: 28px; line-height: 1.7; letter-spacing: 0.5px; }
  .offer-rule { width: 56px; height: 3px; background: var(--gold); margin-top: 6px; }
  .features { list-style: none; margin-top: 18px; }
  .features li {
    display: flex; align-items: center; gap: 8px;
    font-size: 16.5px; font-weight: 400; height: 45.5px; letter-spacing: 0.3px;
  }
  .features .tick { width: 19px; height: 19px; flex: none; }
  .features strong { color: var(--gold); font-weight: 700; }

  .contact { position: absolute; left: 66px; top: 1060px; color: var(--ink); }
  .contact-label { font-weight: 700; font-size: 22px; letter-spacing: 1px; }
  .contact-phone { font-weight: 700; font-size: 43px; margin-top: 4px; letter-spacing: 0.5px; }
  .contact-phone .number { color: var(--white); }
  .contact-web {
    display: flex; align-items: center; gap: 10px;
    font-weight: 600; font-size: 35px; color: var(--white); margin-top: -2px;
  }
  .contact-web svg { width: 30px; height: 30px; }

  .license {
    position: absolute; left: 763px; top: 1000px;
    width: 377px; height: 52px; border-radius: 26px;
    background: var(--gold); border: 3px solid var(--olive);
    display: flex; align-items: center; justify-content: center;
    font-weight: 500; font-size: 38px; color: var(--ink); letter-spacing: 0.5px;
  }
  .program-mark {
    position: absolute; left: 688px; top: 1078px;
    font-weight: 800; font-size: 40px; color: var(--red);
  }
  .divider { position: absolute; left: 1014px; top: 1065px; width: 2px; height: 90px; background: #777; }
  .housing-badge { position: absolute; left: 1040px; top: 1070px; width: 82px; height: 82px; background: var(--ink); }
</style>
</head>
<body>
<main class="flyer">
  <svg class="backdrop" viewBox="0 0 1533 1533" xmlns="http://www.w3.org/2000/svg" aria-hidden="false">
    <defs>
      <linearGradient id="warmRoom" x1="0" y1="0" x2="1" y2="1">
        <stop offset="0" stop-color="var(--photo-warm-a)"/>
        <stop offset="1" stop-color="var(--photo-warm-b)"/>
      </linearGradient>
      <linearGradient id="portrait" x1="0" y1="0" x2="0" y2="1">
        <stop offset="0" stop-color="var(--photo-portrait-a)"/>
        <stop offset="1" stop-color="var(--photo-portrait-b)"/>
      </linearGradient>
    </defs>

    <!-- main photo -->
    <path role="img" aria-label="Photo of a happy couple sitting among moving boxes in their new home"
          d="M870,0 H1533 V915 C1350,985 1050,930 830,765 C660,560 700,200 870,0 Z" fill="url(#warmRoom)"/>
    <path d="M860,0 C680,200 640,575 822,772" fill="none" stroke="var(--blue-line)" stroke-width="14"/>

    <!-- blue band with gold trim -->
    <path d="M80,880 C330,800 620,840 790,940 L780,960 C600,860 330,830 80,885 Z" fill="var(--gold)"/>
    <path d="M0,915 C250,820 560,840 780,965 C1050,1080 1300,1020 1533,930 V1533 H0 Z" fill="var(--blue)"/>
    <path d="M1210,1045 C1330,1030 1450,990 1533,945 V962 C1450,1005 1330,1045 1215,1060 Z" fill="var(--gold)"/>

    <!-- olive footer -->
    <path d="M0,1320 H870 C800,1390 770,1460 750,1533 H0 Z" fill="var(--olive)"/>

    <!-- white corner with gold edge -->
    <path d="M750,1533 C820,1300 1050,1170 1250,1165 C1380,1165 1480,1220 1533,1265 V1533 Z" fill="var(--white)"/>
    <path d="M750,1533 C820,1300 1050,1170 1250,1165 C1380,1165 1480,1220 1533,1265" fill="none" stroke="var(--gold)" stroke-width="10"/>

    <!-- portrait circle -->
    <circle cx="1018" cy="915" r="245" fill="var(--white)"/>
    <circle role="img" aria-label="Portrait of a smiling woman holding up house keys"
            cx="1018" cy="915" r="233" fill="url(#portrait)"/>
  </svg>

  <div class="brand">
    <span class="brand-dot"></span>
    <span class="brand-name">2nd Lane Home Lending</span>
  </div>

  <h1 class="headline">
    <span class="line">Home Equity</span>
    <span class="line">Lines of Credit</span>
    <span class="line line-big">Are <span class="accent">Back!</span></span>
  </h1>

  <section class="offer">
    <h2 class="offer-title">THE BEST DPA PRODUCT<br>ON THE PLANET</h2>
    <div class="offer-rule"></div>
    <ul class="features">
      <li><svg class="tick" viewBox="0 0 20 20"><circle cx="10" cy="10" r="8.5" fill="none" stroke="#d6c232" stroke-width="1.6"/><path d="M6 10.3l2.7 2.7L14 7.6" fill="none" stroke="#d6c232" stroke-width="1.6"/></svg>Lowest Zarn in the Industry -&nbsp;<strong>580 Minimum</strong></li>
      <li><svg class="tick" viewBox="0 0 20 20"><circle cx="10" cy="10" r="8.5" fill="none" stroke="#d6c232" stroke-width="1.6"/><path d="M6 10.3l2.7 2.7L14 7.6" fill="none" stroke="#d6c232" stroke-width="1.6"/></svg>Nothing Down -&nbsp;<strong>100% GTU Purchase Financing</strong></li>
      <li><svg class="tick" viewBox="0 0 20 20"><circle cx="10" cy="10" r="8.5" fill="none" stroke="#d6c232" stroke-width="1.6"/><path d="M6 10.3l2.7 2.7L14 7.6" fill="none" stroke="#d6c232" stroke-width="1.6"/></svg>One Submission, One Approval and One Closing</li>
      <li><svg class="tick" viewBox="0 0 20 20"><circle cx="10" cy="10" r="8.5" fill="none" stroke="#d6c232" stroke-width="1.6"/><path d="M6 10.3l2.7 2.7L14 7.6" fill="none" stroke="#d6c232" stroke-width="1.6"/></svg>No Income Limits, No DTI Restrictions, No Property Restrictions</li>
    </ul>
  </section>

  <section class="contact">
    <p class="contact-label">FOR MORE INFORMATION</p>
    <p class="contact-phone">CALL <span class="number">(800) 471-9026</span></p>
    <p class="contact-web">
      <svg viewBox="0 0 30 30"><circle cx="15" cy="15" r="13" fill="none" stroke="#1d1d1d" stroke-width="2.4"/><ellipse cx="15" cy="15" rx="6" ry="13" fill="none" stroke="#1d1d1d" stroke-width="2.2"/><path d="M2 15h26M4 8.5h22M4 21.5h22M15 2v26" stroke="#1d1d1d" stroke-width="2.2"/></svg>
      www.2ndlanehomes.com
    </p>
  </section>

  <div class="license">RLCB #738160</div>
  <div class="program-mark">KIVO Program</div>
  <div class="divider"></div>
  <div class="housing-badge"></div>
</main>
</body>
</html>
```